Norwegian psychologist service needs a fresh and exiting web site*

Norwegian psychologist service: working with therapy, personal development, mastery and personal growth. Focus: children and teenagers with special needs; family dynamics; group processes; individuals with a need for therapy and personal growth. (Our company name: Fjordlys og samhold (means Mastery and Growth).

We already have a logo for the company, which will be used (will be attached in the project).

The webside is to be structured in 4 pages with roll down curtain menus (the numbers are just for guiding the designer - the should not be added):

Page 1: Om Fjordlys og Samhold (about Mastery and Growth): this is where our business is is presented/described shortly: Lorem Ipsum dolor cit...

Page 2: Tjenester (Services): this is where our 5 service areas are presented:
2.1 Utredning (Investigation, diagnosing): Lorem Ipsum dolor cit...
2.2 Rådgivning (consulting): Lorem Ipsum dolor cit...

2.3 Kurs og work shops (courses and work shops): Lorem Ipsum dolor cit...
2.3a Fjordlys og samhold Tema 1 (T1)
2.3b Fjordlys og samhold Tema 2 (T2)
2.3c Fjordlys og samhold Tema 3 (T3)

2.4 Terapi og utvikling (Therapy and development)
2.4a Fjordlys og samhold for individer (FS1)
2.4b Fjordlys og samhold i familier (FS2)
2.4c Fjordlys og samhold i grupper (FS3)
2.4d Fjordlys og samhold i institusjoner (FS4)

Page 3: Aktuelt (Blog): this is our blog where we share knowledge and articles

Page 4: Kontakt (Contact): This is the contact form page. Contact form should constitute:
- Ditt navn (your name)
- E-post (your e-mail)
- Emne (subject)
- Melding (message/description)

Our project should also include suggestion for handheld units (iPhone, iPad).
Updates

We have both been traveling with work for a while, and then unfortunately both of us got sick on return, so we need a few more days to evaluate and choose design. Kind Regards Arvid & Margit

Target Market(s)

Focus on therapy, learning, mastery and growth for children and teenagers with special needs, within the family dynamics, or in a group setting.
OUR MARKETS:
Private market: individuals, families, groups and health industry institutions (with focus on learning, mastery, growth (as well as growing up) and psychiatry for children and teenagers with special difficulties and needs)
Public institutions: Government institutions, state institutions and municipality institutions (e.g. schools, municipality health service, hospitals) that serve the public (families with children and teenagers with special needs, and where learning, mastery, growth (as well as growing up) and potential psychiatry is an issue).

Number of Pages Required

4 page

Font styles to use
Sans Serif

Colors

Designer to choose colors to be used in the design.

Requirements
Must have
• The website must have 4 pages with roll down curtain menus (we have added a PDF with suggested structure, and headings, with sub menus - see attached PDF drawing.
• The web page must also use the added logo file - and make the web page work well with our logo.
• We would like the website to have a modern look and we would like the site to be associated with typical HIGH END TOP QUALITY private health institutions, but with a stronger focus on human beings (hands, faces etc), and not white coats and doctors. We are psychologists in the private market.
• For instance, if photos are being used - we tend to like "warm" almost art-like, "grainy" two-tone (e.g. sepia) photos to illustrate our focus. If designer can find such photos as part of design, it would be interesting to us. We would like a few photos like that integrated in the design.
• We also want a design suggestion for how the web page should look like and behave on handheld units (e.g. iPhone, iPad).
Nice to have
• If designer could find a number of suitable photos that matches the business idea and design requirements (see description above), that could follow website, that would be good.
• It could also be nice to have graphic symbols that denote the different pages/subpages (subjects)....
• HORSES: we sometimes use horses as a "tool" in therapy sessions. The horse is not necessarily used for riding, but for contact, communication and grooming. PHOTOS: we would like the designer to find an opportunity for using a photo reflecting this cooperation between therapist, child, teenager and horse. It is a bit up to the designer to find a way to do this... Since the horse is only a tool, among many other tools, it does not have to be much - but we want to try and see how it will work with a photo that also reflects this part of our business.

```html
<!DOCTYPE html>
<html lang="no">
<head>
<meta charset="utf-8">
<title>Aktuelt – Fjordlys og samhold</title>
<link href="https://fonts.googleapis.com/css2?family=Jost:wght@300;400;500&family=Arimo:wght@400&display=swap" rel="stylesheet">
<style>
:root{
  --navy:#2a3489;
  --ink:#222;
  --text:#3a3a3a;
  --green:#2f7d3c;
  --panel:#ebebeb;
  --footer:#0b1050;
  --footer-bar:#3b4379;
  --white:#fff;
}
*{margin:0;padding:0;box-sizing:border-box}
html,body{width:1200px;height:2259px;overflow:hidden;background:var(--white)}
body{position:relative;font-family:"Jost",sans-serif;color:var(--text)}
.abs{position:absolute}

.site-header{left:0;top:0;width:1200px;height:171px;
  background:linear-gradient(100deg,#fbe6d6 0%,#fdf0e6 40%,#fcefe6 70%,#fbe9dd 100%)}
.brand{left:119px;top:50px;display:flex;align-items:center;gap:10px;color:var(--navy);
  font-size:30px;font-weight:400;line-height:1.05;width:220px}
.brand-dot{width:20px;height:20px;border-radius:50%;background:var(--navy);flex:none}
.menu-toggle{left:1000px;top:79px;width:37px;height:30px}

.page-title{left:119px;top:220px;font-size:45px;font-weight:400;color:var(--ink)}

.post-title{left:120px;width:630px;font-size:21px;font-weight:500;color:var(--navy);
  line-height:33px;text-transform:uppercase;white-space:nowrap}
.post-photo{left:119px;width:625px;height:280px}
.photo-family{top:404px;background:radial-gradient(ellipse at 45% 55%,#8a8a8a 0%,#4a4a4a 45%,#1f1f1f 100%)}
.photo-crowd{top:1012px;background:radial-gradient(ellipse at 52% 10%,#e6e6e6 0%,#7d7d7d 30%,#3e3e3e 70%,#2a2a2a 100%)}
.post-excerpt{left:121px;width:620px;font-size:19px;font-weight:300;line-height:26.4px;color:var(--text);white-space:nowrap}
.btn-read{width:182px;height:47px;border:1.3px solid var(--navy);border-radius:24px;
  color:var(--navy);font-size:20px;font-weight:400;display:flex;align-items:center;justify-content:center}

.sidebar-title{left:799px;top:357px;font-size:21.5px;font-weight:500;color:var(--ink)}
.sidebar{left:798px;top:401px;width:271px;height:1086px;background:var(--panel);padding:26px 20px 0 23px}
.recent{margin-bottom:16px}
.recent h3{font-size:19px;font-weight:300;line-height:32.5px;color:#444;text-transform:uppercase;white-space:nowrap}
.recent p{margin-top:3px;font-size:16px;font-weight:500;line-height:26.4px;color:#222;white-space:nowrap}
.recent a{color:var(--green);text-decoration:none;font-weight:400}

.site-footer{left:0;top:1868px;width:1200px;height:339px;background:var(--footer);color:var(--white)}
.footer-brand{left:106px;top:120px;display:flex;align-items:center;gap:10px;font-size:31px;
  line-height:1.05;width:220px;font-weight:400}
.footer-brand .brand-dot{background:var(--white)}
.footer-col h4{font-size:23px;font-weight:400;margin-bottom:10px}
.footer-col ul{list-style:none;font-family:"Arimo",sans-serif;font-size:14.5px;line-height:26.4px}
.col-contact{left:400px;top:91px}
.col-pages{left:679px;top:91px}
.col-services{left:930px;top:86px}
.footer-bar{left:0;top:2207px;width:1200px;height:52px;background:var(--footer-bar);color:#dfe1ee}
.copyright{left:106px;top:17px;font-size:13px;font-weight:300}
.social{left:1003px;top:14px;display:flex;gap:10px}
.social span{width:24px;height:24px;border-radius:50%;background:#8c91b4}
</style>
</head>
<body>

<header class="site-header abs">
  <div class="brand abs"><span class="brand-dot"></span>Fjordlys og samhold</div>
  <svg class="menu-toggle abs" viewBox="0 0 37 30" aria-label="Meny">
    <rect x="0" y="0" width="37" height="3" fill="#2a3489"/>
    <rect x="10" y="13" width="27" height="3" fill="#2a3489"/>
    <rect x="0" y="26" width="37" height="3" fill="#2a3489"/>
  </svg>
</header>

<h1 class="page-title abs">Aktuelt</h1>

<h2 class="post-title abs" style="top:327px">Lorem ipsum dolor sit amet, consectetur adipiscing<br>elit, sed do eiusmod tempor incididunt aliqua.</h2>
<div class="post-photo photo-family abs" role="img" aria-label="Svart-hvitt foto av en smilende familie som holder rundt hverandre"></div>
<p class="post-excerpt abs" style="top:702px">Lorem ipsum dolor sit amet, consectetur adipiscing elit, sed do eiusmod<br>tempor incididunt ut labore et dolore magna aliqua. Quis ipsum sus-<br>pendisse ultrices gravida. Risus commodo viverra maecenas accumsan<br>lacus vel facilisis.</p>
<a class="btn-read abs" style="left:119px;top:832px">Read More</a>

<h2 class="post-title abs" style="top:935px">Lorem ipsum dolor sit amet, consectetur adipiscing<br>elit, sed do eiusmod tempor incididunt aliqua.</h2>
<div class="post-photo photo-crowd abs" role="img" aria-label="Svart-hvitt foto av et barn på skuldrene til en voksen foran en folkemengde i motlys"></div>
<p class="post-excerpt abs" style="top:1310px">Lorem ipsum dolor sit amet, consectetur adipiscing elit, sed do eiusmod<br>tempor incididunt ut labore et dolore magna aliqua. Quis ipsum sus-<br>pendisse ultrices gravida. Risus commodo viverra maecenas accumsan<br>lacus vel facilisis.</p>
<a class="btn-read abs" style="left:116px;top:1440px">Read More</a>

<h2 class="sidebar-title abs">SISTE INNLEGG</h2>
<aside class="sidebar abs">
  <div class="recent">
    <h3>Lorem ipsum dolor sit<br>amet, consectetur<br>adipiscing elit, sed do<br>eiusmod</h3>
    <p>Lorem ipsum dolor sit amet,<br>consectetur adipiscing elit,<br>sed do eiusmod tempor inc-<br>ididunt &nbsp;<a>.. Read More..</a></p>
  </div>
  <div class="recent">
    <h3>Lorem ipsum dolor sit<br>amet, consectetur<br>adipiscing elit, sed do<br>eiusmod</h3>
    <p>Lorem ipsum dolor sit amet,<br>consectetur adipiscing elit,<br>sed do eiusmod tempor inc-<br>ididunt &nbsp;<a>.. Read More..</a></p>
  </div>
  <div class="recent">
    <h3>Lorem ipsum dolor sit<br>amet, consectetur<br>adipiscing elit, sed do<br>eiusmod</h3>
    <p>Lorem ipsum dolor sit amet,<br>consectetur adipiscing elit,<br>sed do eiusmod tempor inc-<br>ididunt &nbsp;<a>.. Read More..</a></p>
  </div>
</aside>

<footer class="site-footer abs">
  <div class="footer-brand abs"><span class="brand-dot"></span>Fjordlys og samhold</div>
  <div class="footer-col col-contact abs">
    <h4>Contact Us</h4>
    <ul>
      <li>Dummy Address</li>
      <li>Lorem Ipsum Sit Amet</li>
      <li>Dummy Pin</li>
      <li>Dummy place</li>
      <li>Telephone : +47 22 14 58 90</li>
      <li>Email : post@fjordlys-samhold.no</li>
    </ul>
  </div>
  <div class="footer-col col-pages abs">
    <h4>Pages</h4>
    <ul>
      <li>Om Fjordlys og Samhold</li>
      <li>Tjenester</li>
      <li>Aktuelt</li>
      <li>Kontakt</li>
    </ul>
  </div>
  <div class="footer-col col-services abs">
    <h4>Tjenester</h4>
    <ul>
      <li>Utredning</li>
      <li>Rådgivning</li>
      <li>Kurs og workshops</li>
      <li>Terapi og utvikling</li>
    </ul>
  </div>
</footer>
<div class="footer-bar abs">
  <p class="copyright abs">Copyright Fjordlys og Samhold © 2020. All Rights Reserved</p>
  <div class="social abs"><span></span><span></span><span></span></div>
</div>

</body>
</html>
```